KV HOLDING Business Cards

I need business cards for "KV Holding group LLC" doublesided... logo on the back (also include logo on front)
logo attached to project... i have jpg up..
Company Info:
418 East Marlow Avenue, Suite 7B
Chicago, Illinois 60617
facsimile 312-555-0188 (list fax, address, website on all cards.)
www.kvholdinggroup.example
Three different people on cards:
Dorian P. Kell, CPA MST
Principal
ofc 312-555-0142
mobile 312-555-0167
dorianpkell@kvholdinggroup.example
Marcus T. Brenholt, CPA MST
Principal
marcustbrenholt@kvholdinggroup.example
mobile 708-555-0119
ofc 312-555-0142
Nigel F Carrow
Principal
ofc 312-555-0142
no mobile
nigelfcarrow@kvholdinggroup.example
I have multiple projects listed.. see below:
Business cards for amber gate equity llc
letterhead
envelopes
Business cards for KV Holding LLC
letterhead
envelopes
Target Market(s)
rich people
Industry/Entity Type
Business
Look and feel

```html
<!DOCTYPE html>
<html lang="en">
<head>
<meta charset="utf-8">
<title>KV Holding Group LLC – Business Card</title>
<link rel="stylesheet" href="https://fonts.googleapis.com/css2?family=Cinzel:wght@400&family=Arimo:wght@400&display=swap">
<style>
  :root {
    --navy: #1c3f73;
    --navy-deep: #14305c;
    --navy-light: #2a5290;
    --ink: #1a1a1a;
    --paper: #ffffff;
    --paper-shade: #eef0f3;
    --stage: #ffffff;
  }
  * { box-sizing: border-box; margin: 0; padding: 0; }
  html, body { width: 1200px; height: 900px; overflow: hidden; background: var(--stage); }
  .canvas {
    width: 1200px; height: 900px;
    display: flex; align-items: center; justify-content: center; gap: 40px;
  }
  .card {
    width: 540px; height: 310px; border-radius: 26px;
    position: relative; overflow: hidden;
    box-shadow: 0 10px 28px rgba(0,0,0,0.18);
  }

  /* Front */
  .card-front {
    background: linear-gradient(160deg, var(--navy-deep) 0%, var(--navy) 55%, var(--navy-light) 100%);
  }
  .card-front .brand-mark {
    position: absolute; left: 50%; top: 56px; transform: translateX(-50%);
    width: 110px; height: 110px; border-radius: 50%;
    background: var(--paper);
  }
  .card-front .brand-name {
    position: absolute; left: 0; right: 0; top: 206px; text-align: center;
    font-family: "Cinzel", serif; font-weight: 400; font-size: 36px;
    color: var(--paper); letter-spacing: 1px;
  }

  /* Back */
  .card-back {
    background: linear-gradient(180deg, var(--paper) 0%, var(--paper-shade) 100%);
    color: var(--ink);
  }
  .card-back .brand {
    position: absolute; left: 34px; top: 36px;
    display: flex; align-items: center; gap: 10px;
  }
  .card-back .brand-mark {
    width: 34px; height: 34px; border-radius: 50%; background: var(--navy);
  }
  .card-back .brand-name {
    font-family: "Cinzel", serif; font-weight: 400; font-size: 19px; color: var(--navy);
  }
  .person {
    position: absolute; right: 30px; top: 30px; text-align: right;
    font-family: "Arimo", sans-serif;
  }
  .person .name { font-size: 14px; color: var(--navy); }
  .person .role { font-size: 10px; color: var(--ink); margin-top: 3px; }

  .contacts {
    position: absolute; left: 30px; top: 112px;
    font-family: "Arimo", sans-serif; font-size: 13.5px; line-height: 17px;
    list-style: none;
  }
  .contacts li { display: flex; align-items: flex-start; gap: 5px; }
  .contacts .group-gap { margin-top: 8px; }
  .contacts svg { width: 13px; height: 13px; flex: none; margin-top: 2px; fill: var(--navy); }

  .band-rule {
    position: absolute; left: 0; right: 0; bottom: 32px; height: 3px; background: #0d1f3c;
  }
  .band {
    position: absolute; left: 0; right: 0; bottom: 0; height: 32px; background: var(--navy);
  }
</style>
</head>
<body>
<main class="canvas">
  <section class="card card-front" aria-label="Card front">
    <span class="brand-mark" aria-hidden="true"></span>
    <p class="brand-name">KV Holding Group LLC</p>
  </section>

  <section class="card card-back" aria-label="Card back">
    <div class="brand">
      <span class="brand-mark" aria-hidden="true"></span>
      <span class="brand-name">KV Holding Group LLC</span>
    </div>

    <div class="person">
      <p class="name">Dorian P. Kell, CPA MST</p>
      <p class="role">Principal</p>
    </div>

    <ul class="contacts">
      <li>
        <svg viewBox="0 0 24 24" aria-hidden="true"><path d="M6.6 10.8a15.1 15.1 0 0 0 6.6 6.6l2.2-2.2c.3-.3.7-.4 1-.2 1.1.4 2.3.6 3.6.6.6 0 1 .4 1 1V20c0 .6-.4 1-1 1A17 17 0 0 1 3 4c0-.6.4-1 1-1h3.5c.6 0 1 .4 1 1 0 1.3.2 2.5.6 3.6.1.3 0 .7-.2 1z"/></svg>
        <span>312-555-0142</span>
      </li>
      <li>
        <svg viewBox="0 0 24 24" aria-hidden="true"><path d="M7 2h10a2 2 0 0 1 2 2v16a2 2 0 0 1-2 2H7a2 2 0 0 1-2-2V4a2 2 0 0 1 2-2zm0 3v12h10V5zm5 13.5a1 1 0 1 0 0 2 1 1 0 0 0 0-2z"/></svg>
        <span>312-555-0167</span>
      </li>
      <li>
        <svg viewBox="0 0 24 24" aria-hidden="true"><path d="M7 2h10v5H7zM4 8h16a2 2 0 0 1 2 2v7h-4v5H6v-5H2v-7a2 2 0 0 1 2-2zm4 8v4h8v-4z"/></svg>
        <span>312-555-0188</span>
      </li>
      <li class="group-gap">
        <svg viewBox="0 0 24 24" aria-hidden="true"><path d="M12 2a10 10 0 1 0 0 20 10 10 0 0 0 0-20zm6.9 9h-3a15 15 0 0 0-1.3-5.7A8 8 0 0 1 18.9 11zM12 4c.9 1.2 1.8 3.7 1.9 7h-3.8c.1-3.3 1-5.8 1.9-7zM9.4 5.3A15 15 0 0 0 8.1 11h-3a8 8 0 0 1 4.3-5.7zM5.1 13h3a15 15 0 0 0 1.3 5.7A8 8 0 0 1 5.1 13zM12 20c-.9-1.2-1.8-3.7-1.9-7h3.8c-.1 3.3-1 5.8-1.9 7zm2.6-1.3a15 15 0 0 0 1.3-5.7h3a8 8 0 0 1-4.3 5.7z"/></svg>
        <span>www.kvholdinggroup.example</span>
      </li>
      <li>
        <svg viewBox="0 0 24 24" aria-hidden="true"><path d="M2 5h20v14H2zm2 2v.5l8 5 8-5V7zm0 2.9V17h16V9.9l-8 5z"/></svg>
        <span>dorianpkell@kvholdinggroup.example</span>
      </li>
      <li class="group-gap">
        <svg viewBox="0 0 24 24" aria-hidden="true"><path d="M12 3 2 12h3v8h5v-5h4v5h5v-8h3z"/></svg>
        <span>418 East Marlow Avenue, Suite 7B<br>Chicago, Illinois 60617 facsimile</span>
      </li>
    </ul>

    <div class="band-rule" aria-hidden="true"></div>
    <div class="band" aria-hidden="true"></div>
  </section>
</main>
</body>
</html>
```